Dane Calloway Photography

Would like the Business card to have a cool logo. I’m targeting wedding/ engagement: portrait photography. My phone number on it. And my business email address.

Target Market(s)

Wedding/portrait/engagement photography.

```html
<!DOCTYPE html>
<html lang="en">
<head>
<meta charset="utf-8">
<title>Dane Calloway Photography — Business Card</title>
<link rel="stylesheet" href="https://fonts.googleapis.com/css2?family=Jost:wght@400;500&display=swap">
<style>
  :root {
    --backdrop: #2a2520;
    --card: #050505;
    --card-edge: #2c2c2c;
    --gold: #e3a43f;
    --silver: #b3b2aa;
    --silver-soft: #9d9c95;
  }
  html, body {
    margin: 0;
    padding: 0;
    width: 1200px;
    height: 1189px;
    overflow: hidden;
    background: var(--backdrop);
  }
  .canvas {
    position: relative;
    width: 1200px;
    height: 1189px;
  }
  .business-card {
    position: absolute;
    left: 100px;
    top: 325px;
    width: 1000px;
    height: 540px;
    background: var(--card);
    border: 2px solid var(--card-edge);
    border-radius: 56px;
    box-sizing: border-box;
    font-family: "Jost", sans-serif;
  }
  .brand-lockup {
    position: absolute;
    left: 70px;
    top: 190px;
    width: 400px;
    display: flex;
    align-items: center;
    justify-content: center;
    gap: 16px;
  }
  .brand-dot {
    width: 22px;
    height: 22px;
    border-radius: 50%;
    background: var(--gold);
    flex: none;
  }
  .brand-name {
    margin: 0;
    color: var(--gold);
    font-weight: 500;
    font-size: 40px;
    line-height: 1.15;
    letter-spacing: 0.5px;
  }
  .contact {
    position: absolute;
    left: 555px;
    top: 150px;
    color: var(--silver);
  }
  .contact-name {
    margin: 0;
    font-weight: 400;
    font-size: 46px;
    letter-spacing: 1px;
    line-height: 1;
  }
  .contact-email {
    margin: 8px 0 0;
    font-size: 23px;
    color: var(--silver-soft);
    letter-spacing: 0.5px;
  }
  .contact-address {
    margin: 30px 0 0;
    font-size: 23px;
    line-height: 1.4;
    color: var(--silver-soft);
    text-transform: uppercase;
    letter-spacing: 0.5px;
  }
  .contact-phone {
    margin: 22px 0 0;
    font-size: 35px;
    letter-spacing: 1px;
  }
</style>
</head>
<body>
<main class="canvas">
  <section class="business-card">
    <div class="brand-lockup">
      <span class="brand-dot"></span>
      <h1 class="brand-name">Dane Calloway<br>Photography</h1>
    </div>
    <div class="contact">
      <h2 class="contact-name">DANE CALLOWAY</h2>
      <p class="contact-email">hello@danecalloway.net</p>
      <p class="contact-address">Elm Avenue 31420<br>Lakeview 07263</p>
      <p class="contact-phone">555 0142 7731</p>
    </div>
  </section>
</main>
</body>
</html>
```